Business Card Design for new logo

Business card Design for new logo. Follow colors from logo.
The company has offices in multiple comtries
Want to have some bulltes on the countries and also on the main services

Something like
USA*Dominican Republic*LATAM

Consulting*Healthcare IT*Tranformation

Industry/Entity Type

Information Technology

Contact Information for Business Card

Address, Phones, countries, name and position

Miron castell

Founder and CEO

947 Quarry Ln
Mill haven, PA 16835

Mcastell@novelquin.com

www.novelquin.com

717-352-6081

828-444-4444

```html
<!DOCTYPE html>
<html lang="en">
<head>
<meta charset="utf-8">
<title>Novelquin Health — Business Card</title>
<link rel="stylesheet" href="https://fonts.googleapis.com/css2?family=Roboto:wght@400;500;700&display=swap">
<style>
  :root {
    --canvas: #2a2a2c;
    --card-black: #0c0c0d;
    --card-black-soft: #1d1e21;
    --brand-blue: #4a7fc8;
    --brand-orange: #e5824a;
    --brand-orange-soft: #e9a464;
    --paper: #ffffff;
    --text-light: #f2f2f2;
  }
  * { margin: 0; padding: 0; box-sizing: border-box; }
  html, body { width: 1200px; height: 1101px; overflow: hidden; }
  body {
    background: var(--canvas);
    font-family: "Roboto", Arial, sans-serif;
    position: relative;
  }
  .card {
    position: absolute;
    left: 180px;
    width: 840px;
    height: 480px;
    overflow: hidden;
    border-radius: 4px;
  }
  /* Back of card */
  .card-back {
    top: 50px;
    background: radial-gradient(ellipse at 52% 40%, var(--card-black-soft) 0%, var(--card-black) 70%);
  }
  .brand {
    position: absolute;
    display: flex;
    align-items: center;
    gap: 14px;
    color: var(--brand-blue);
    font-weight: 500;
    white-space: nowrap;
  }
  .brand-dot {
    border-radius: 50%;
    background: var(--brand-blue);
    flex: none;
  }
  .card-back .brand { top: 120px; left: 0; right: 0; justify-content: center; font-size: 40px; }
  .card-back .brand-dot { width: 22px; height: 22px; }
  .bullet-list {
    position: absolute;
    list-style: none;
    color: var(--brand-orange);
    font-size: 21px;
    line-height: 36px;
  }
  .bullet-list li::before {
    content: "";
    display: inline-block;
    width: 7px; height: 7px;
    border-radius: 50%;
    background: var(--brand-blue);
    margin-right: 10px;
    vertical-align: middle;
  }
  .countries { left: 125px; top: 260px; }
  .services { left: 520px; top: 205px; }

  /* Front of card */
  .card-front { top: 570px; background: var(--card-black); }
  .front-wave { position: absolute; inset: 0; }
  .person {
    position: absolute;
    left: 70px; top: 66px;
  }
  .person-name { color: var(--brand-orange); font-size: 30px; font-weight: 700; }
  .person-title { color: var(--text-light); font-size: 21px; margin-top: 4px; }
  .contact-list {
    position: absolute;
    left: 60px; top: 200px;
    list-style: none;
    color: var(--text-light);
    font-size: 22px;
  }
  .contact-list li { display: flex; align-items: flex-start; gap: 14px; margin-bottom: 11px; line-height: 28px; }
  .contact-icon {
    width: 28px; height: 28px; flex: none;
    border-radius: 50%;
    background: var(--brand-orange);
    display: flex; align-items: center; justify-content: center;
  }
  .contact-icon svg { width: 16px; height: 16px; fill: var(--card-black); }
  .card-front .brand { right: 46px; top: 265px; font-size: 38px; }
  .card-front .brand-dot { width: 20px; height: 20px; }
</style>
</head>
<body>

<section class="card card-back">
  <div class="brand"><span class="brand-dot"></span>Novelquin Health</div>
  <ul class="bullet-list countries">
    <li>USA</li>
    <li>Dominican Republic</li>
    <li>LATAM</li>
  </ul>
  <ul class="bullet-list services">
    <li>Consulting</li>
    <li>Healthcare IT</li>
    <li>Tranformation</li>
  </ul>
</section>

<section class="card card-front">
  <svg class="front-wave" viewBox="0 0 840 480" preserveAspectRatio="none" aria-hidden="true">
    <path fill="var(--brand-blue)" d="M548 0 C488 60 478 130 428 190 C365 262 318 332 331 400 C340 446 372 470 400 480 L840 480 L840 0 Z"/>
    <path fill="var(--brand-orange)" d="M548 0 C488 60 488 130 438 190 C376 262 331 332 343 400 C351 446 384 470 412 480 L840 480 L840 0 Z"/>
    <path fill="var(--paper)" d="M555 0 C495 60 498 130 448 190 C386 262 343 332 355 400 C363 446 396 470 424 480 L840 480 L840 0 Z"/>
  </svg>

  <div class="person">
    <div class="person-name">Miron castell</div>
    <div class="person-title">Founder and CEO</div>
  </div>

  <ul class="contact-list">
    <li><span class="contact-icon"><svg viewBox="0 0 24 24"><path d="M6.6 10.8a15 15 0 0 0 6.6 6.6l2.2-2.2a1 1 0 0 1 1-.25 11.4 11.4 0 0 0 3.6.57 1 1 0 0 1 1 1V20a1 1 0 0 1-1 1A17 17 0 0 1 3 4a1 1 0 0 1 1-1h3.5a1 1 0 0 1 1 1c0 1.25.2 2.45.57 3.57a1 1 0 0 1-.25 1z"/></svg></span>717-352-6081</li>
    <li><span class="contact-icon"><svg viewBox="0 0 24 24"><path d="M7 2h10a2 2 0 0 1 2 2v16a2 2 0 0 1-2 2H7a2 2 0 0 1-2-2V4a2 2 0 0 1 2-2zm0 3v13h10V5zm5 14.2a1 1 0 1 0 0 .01z"/></svg></span>828-444-4444</li>
    <li><span class="contact-icon"><svg viewBox="0 0 24 24"><path d="M3 5h18a1 1 0 0 1 1 1v12a1 1 0 0 1-1 1H3a1 1 0 0 1-1-1V6a1 1 0 0 1 1-1zm9 7.5L4 7.5V9l8 5 8-5V7.5z"/></svg></span>Mcastell@novelquin.com</li>
    <li><span class="contact-icon"><svg viewBox="0 0 24 24"><path d="M12 2a10 10 0 1 0 0 20 10 10 0 0 0 0-20zm6.9 6h-2.9a15 15 0 0 0-1.4-3.6A8 8 0 0 1 18.9 8zM12 4c.8 1.2 1.5 2.5 1.9 4h-3.8c.4-1.5 1.1-2.8 1.9-4zM4.3 14a8 8 0 0 1 0-4h3.4a16 16 0 0 0 0 4zm.8 2h2.9c.3 1.3.8 2.5 1.4 3.6A8 8 0 0 1 5.1 16zM8 8H5.1a8 8 0 0 1 4.3-3.6C8.8 5.5 8.3 6.7 8 8zm4 12c-.8-1.2-1.5-2.5-1.9-4h3.8c-.4 1.5-1.1 2.8-1.9 4zm2.3-6H9.7a14 14 0 0 1 0-4h4.6a14 14 0 0 1 0 4zm.3 5.6c.6-1.1 1.1-2.3 1.4-3.6h2.9a8 8 0 0 1-4.3 3.6zm1.7-5.6a16 16 0 0 0 0-4h3.4a8 8 0 0 1 0 4z"/></svg></span>www.novelquin.com</li>
    <li><span class="contact-icon"><svg viewBox="0 0 24 24"><path d="M12 2a7 7 0 0 0-7 7c0 5.2 7 13 7 13s7-7.8 7-13a7 7 0 0 0-7-7zm0 9.5a2.5 2.5 0 1 1 0-5 2.5 2.5 0 0 1 0 5z"/></svg></span><span>947 Quarry Ln<br>Mill haven, PA 16835</span></li>
  </ul>

  <div class="brand"><span class="brand-dot"></span>Novelquin Health</div>
</section>

</body>
</html>
```